KTR Engineering Business Card Design

We’re looking for an elegant, clean, and timeless business card design that communicates experience, capability, and reliability.

KTR Engineering was established in 1995 , we are a Government Contracting company providing Professional Services to the Ministry of Harbor Works, Frontier Stewardship and the Waypoint Consortium. Our capabilities include: Acquisition & Program Management; Intelligence & Security Operations; Cyber, IT & Network Operations; Lifecycle Logistics & Asset Readiness; C5ISR Systems Engineering & Sustainment.

We want the card to reflect a straightforward, confident approach to business. The design should feel polished and professional without being flashy or overly corporate.

Design Direction
Clean, sophisticated, and uncluttered
Elegant but understated
Strong typography and thoughtful spacing
A timeless aesthetic rather than something overly trendy
Confident and established, with a sense of substance
Easy to read and practical in a real-world business setting

The overall impression should be: “These are experienced professionals who know what they’re doing, do what they say, and can be relied upon.”

We’re open to creative interpretations. The finished card should feel distinctive through its typography, proportions, layout, and attention to detail rather than through excessive graphics or visual effects.

We’re looking for a design that would make a potential client immediately feel that they’re dealing with a capable, trustworthy, and established company.

Company Colors: Navy and Gold/Yellow (but you do not need to use these colors on the card)
Company Name: KTR Engineering Associates, Inc. (known as KTR Engineering)
Website: ktrengineering.example
Company Logo: Navy & Gold (other variations attached)

```html
<!DOCTYPE html>
<html lang="en">
<head>
<meta charset="UTF-8">
<title>KTR Engineering Business Card</title>
<link rel="stylesheet" href="https://fonts.googleapis.com/css2?family=Poppins:wght@400;500;800&display=swap">
<style>
  :root {
    --navy: #232d5f;
    --gold: #f9e04b;
    --white: #ffffff;
    --ink-grey: #555a60;
    --stage: #26272b;
  }
  * { box-sizing: border-box; margin: 0; padding: 0; }
  html, body {
    width: 1200px;
    height: 1200px;
    overflow: hidden;
    background: var(--stage);
    font-family: "Poppins", sans-serif;
  }
  .sheet {
    width: 1200px;
    height: 1200px;
    display: flex;
    flex-direction: column;
    align-items: center;
    justify-content: center;
    gap: 64px;
  }
  .card {
    position: relative;
    width: 900px;
    height: 514px;
    overflow: hidden;
    box-shadow: 0 18px 40px rgba(0,0,0,0.45);
  }
  .card--front {
    background: var(--navy);
    color: var(--white);
  }
  .card--back {
    background: var(--white);
    color: var(--navy);
  }
  .wordmark {
    font-weight: 800;
    letter-spacing: -2px;
    line-height: 1;
  }
  .card--front .wordmark {
    position: absolute;
    top: 150px;
    left: 0;
    right: 0;
    text-align: center;
    font-size: 150px;
    color: var(--white);
  }
  .tagline {
    position: absolute;
    top: 372px;
    left: 0;
    right: 0;
    text-align: center;
    font-size: 21px;
    font-weight: 400;
    letter-spacing: 0.6px;
  }
  .card--back .wordmark {
    position: absolute;
    top: 160px;
    left: 80px;
    font-size: 130px;
    color: var(--navy);
  }
  .divider {
    position: absolute;
    left: 450px;
    top: 110px;
    width: 2px;
    height: 240px;
    background: var(--navy);
  }
  .person {
    position: absolute;
    left: 485px;
    top: 118px;
  }
  .person__name {
    font-size: 30px;
    font-weight: 800;
    color: var(--navy);
    letter-spacing: 0.5px;
    line-height: 1.1;
  }
  .person__title {
    font-size: 24px;
    font-weight: 400;
    color: var(--ink-grey);
    line-height: 1.1;
  }
  .contacts {
    position: absolute;
    left: 485px;
    top: 222px;
    list-style: none;
    display: flex;
    flex-direction: column;
    gap: 14px;
  }
  .contacts__item {
    display: flex;
    align-items: center;
    gap: 16px;
    font-size: 22px;
    color: var(--ink-grey);
    font-weight: 400;
    white-space: nowrap;
  }
  .contacts__icon {
    width: 30px;
    height: 30px;
    flex: none;
  }
  .address {
    position: absolute;
    left: 0;
    right: 0;
    top: 412px;
    text-align: center;
    font-size: 24px;
    color: var(--ink-grey);
    font-weight: 400;
  }
</style>
</head>
<body>
  <main class="sheet">
    <section class="card card--front" aria-label="Card front">
      <div class="wordmark">KTR</div>
      <p class="tagline">Three Decades of Trusted Service with Proven Results</p>
    </section>

    <section class="card card--back" aria-label="Card back">
      <div class="wordmark">KTR</div>
      <div class="divider"></div>
      <div class="person">
        <p class="person__name">ALEX MORROW</p>
        <p class="person__title">Manager</p>
      </div>
      <ul class="contacts">
        <li class="contacts__item">
          <svg class="contacts__icon" viewBox="0 0 30 30" aria-hidden="true">
            <circle cx="15" cy="15" r="15" fill="var(--gold)"/>
            <path d="M11 8.5c.8-.4 1.6 0 2 .8l1 2c.3.7.1 1.4-.5 1.8l-.8.5c.6 1.6 1.6 2.9 3 3.9l.7-.6c.6-.5 1.4-.5 1.9.1l1.4 1.6c.5.6.5 1.5-.1 2l-1 .9c-.8.7-2 .8-3 .3-3.3-1.8-5.6-4.8-6.4-8.5-.2-1.1.2-2.2 1-2.9z" fill="var(--navy)"/>
          </svg>
          <span>555-014-2270</span>
        </li>
        <li class="contacts__item">
          <svg class="contacts__icon" viewBox="0 0 30 30" aria-hidden="true">
            <circle cx="15" cy="15" r="15" fill="var(--gold)"/>
            <rect x="8" y="10" width="14" height="10" fill="none" stroke="var(--navy)" stroke-width="1.6"/>
            <path d="M8 10l7 6 7-6" fill="none" stroke="var(--navy)" stroke-width="1.6"/>
          </svg>
          <span>youremail@mailbox.example</span>
        </li>
        <li class="contacts__item">
          <svg class="contacts__icon" viewBox="0 0 30 30" aria-hidden="true">
            <circle cx="15" cy="15" r="15" fill="var(--gold)"/>
            <g fill="none" stroke="var(--navy)" stroke-width="1.3">
              <circle cx="15" cy="15" r="7.5"/>
              <ellipse cx="15" cy="15" rx="3.3" ry="7.5"/>
              <path d="M7.5 15h15M9 11h12M9 19h12"/>
            </g>
          </svg>
          <span>www.ktrengineering.example</span>
        </li>
      </ul>
      <p class="address">1840 Harbor Lane, Suite 310, Bayview, VA 23000</p>
    </section>
  </main>
</body>
</html>
```